Need a book cover design for a Lumora Book on Herbal Remedies

I need a book cover for my new ebook, here are the details:
Title: Meadow Cures
Sub-Heading: Buried Ancient Garden Tonics
Reclaiming the Wisdom of Roots for Everyday Wellness and Strength
Author: Nora Belcourt

```html
<!DOCTYPE html>
<html lang="en">
<head>
<meta charset="utf-8">
<title>Meadow Cures — Nora Belcourt</title>
<link rel="stylesheet" href="https://fonts.googleapis.com/css2?family=Cinzel:wght@700&family=Libre+Baskerville:ital,wght@0,400;0,700;1,400&display=swap">
<style>
  :root {
    --page-bg: #f1efea;
    --frame-green: #a9c28b;
    --cream: #f6f3e6;
    --leaf-deep: #4f8a4a;
    --leaf-mid: #86b26b;
    --leaf-light: #c9ddb0;
    --title-green: #3f7a45;
    --subtitle-orange: #c0653c;
    --author-green: #4c7d47;
  }
  * { box-sizing: border-box; margin: 0; padding: 0; }
  html, body {
    width: 1200px;
    height: 800px;
    overflow: hidden;
    background: var(--page-bg);
  }
  .canvas {
    position: relative;
    width: 1200px;
    height: 800px;
    display: flex;
    align-items: center;
    justify-content: center;
  }
  .book-cover {
    position: relative;
    width: 534px;
    height: 800px;
    background: var(--frame-green);
    padding: 16px;
  }
  .cover-inner {
    position: relative;
    width: 100%;
    height: 100%;
    background: var(--cream);
    overflow: hidden;
  }
  .botanical-art {
    position: absolute;
    inset: 0;
    background:
      radial-gradient(ellipse at 20% 25%, var(--leaf-mid) 0%, transparent 45%),
      radial-gradient(ellipse at 80% 30%, #b97a4a 0%, transparent 30%),
      radial-gradient(ellipse at 25% 75%, var(--leaf-deep) 0%, transparent 40%),
      radial-gradient(ellipse at 78% 78%, var(--leaf-mid) 0%, transparent 42%),
      radial-gradient(ellipse at 50% 95%, var(--cream) 0%, transparent 45%),
      linear-gradient(180deg, var(--leaf-light) 0%, #d8e6c4 50%, #e6ecd6 100%);
  }
  .title-medallion {
    position: absolute;
    left: 50%;
    top: 300px;
    width: 350px;
    height: 350px;
    transform: translate(-50%, -50%);
    border-radius: 50%;
    background: var(--cream);
    border: 3px solid var(--frame-green);
    box-shadow: 0 0 0 6px var(--cream), 0 0 0 8px var(--frame-green);
    display: flex;
    flex-direction: column;
    align-items: center;
    justify-content: center;
    text-align: center;
    padding: 0 40px;
  }
  .book-title {
    font-family: "Cinzel", serif;
    font-weight: 700;
    color: var(--title-green);
    font-size: 46px;
    line-height: 1.02;
    letter-spacing: 1px;
  }
  .title-rule {
    width: 200px;
    height: 2px;
    background: var(--subtitle-orange);
    margin: 16px 0 12px;
  }
  .book-subtitle {
    font-family: "Libre Baskerville", serif;
    font-weight: 700;
    color: var(--subtitle-orange);
    font-size: 14px;
    line-height: 1.3;
  }
  .book-author {
    position: absolute;
    left: 44px;
    bottom: 32px;
    font-family: "Libre Baskerville", serif;
    font-size: 24px;
    color: var(--author-green);
  }
</style>
</head>
<body>
  <main class="canvas">
    <section class="book-cover">
      <div class="cover-inner">
        <div class="botanical-art" role="img" aria-label="Illustrated border of herbs, leaves and wildflowers in greens, orange, purple and yellow"></div>
        <div class="title-medallion">
          <h1 class="book-title">Meadow<br>Cures</h1>
          <div class="title-rule"></div>
          <p class="book-subtitle">Buried Ancient Garden Tonics Reclaiming the Wisdom of Roots for Everyday Wellness and Strength</p>
        </div>
        <p class="book-author">Nora Belcourt</p>
      </div>
    </section>
  </main>
</body>
</html>
```